Business cards for law firm with global theme

I'd like business cards with contact info for two offices. They should include the colors and font of the new logo design, which is a stylized globe with an "F" in it. The feel should be very modern and professional.

```html
<!DOCTYPE html>
<html lang="en">
<head>
<meta charset="utf-8">
<title>Marvella Law – Business Cards</title>
<link href="https://fonts.googleapis.com/css2?family=Poppins:wght@400;500;600;700&display=swap" rel="stylesheet">
<style>
  :root{
    --navy:#1b457c;
    --navy-deep:#163a69;
    --sky:#2ea3df;
    --ink:#1d3f72;
    --paper:#ffffff;
    --ghost:#e7e9ef;
    --stage:#2b2b2d;
  }
  *{box-sizing:border-box;margin:0;padding:0}
  html,body{width:1200px;height:880px;overflow:hidden}
  body{background:var(--stage);font-family:'Poppins',sans-serif;position:relative}

  .card{position:absolute;width:600px;height:343px;border-radius:18px;overflow:hidden}
  .card--front{left:50px;top:60px;background:var(--navy)}
  .card--back{left:550px;top:477px;background:var(--paper)}

  .decor-circle{position:absolute;border-radius:50%}
  .card--front .decor-circle{width:300px;height:300px;right:-40px;top:-90px;background:#234f8a}
  .card--back .decor-circle{width:230px;height:230px;right:70px;top:-40px;background:var(--ghost)}

  /* front brand lockup */
  .front-lockup{position:absolute;left:0;right:0;top:100px;text-align:center}
  .front-lockup .mark-dot{display:block;width:64px;height:64px;border-radius:50%;background:var(--sky);margin:0 auto 14px}
  .brand-name{font-weight:600;letter-spacing:2px;text-transform:uppercase;line-height:1}
  .front-lockup .brand-name{color:#fff;font-size:34px}
  .rule{display:block;height:2px;background:var(--sky);margin:12px auto 0}
  .front-lockup .rule{width:300px}

  /* back brand lockup */
  .back-lockup{position:absolute;left:40px;top:58px;display:flex;align-items:center;gap:20px}
  .back-lockup .mark-dot{width:70px;height:70px;border-radius:50%;background:var(--sky)}
  .back-lockup .brand-name{color:var(--ink);font-size:30px}
  .back-lockup .rule{width:260px;margin-left:0}

  .offices{position:absolute;left:60px;top:172px;width:500px}
  .office{display:flex;align-items:center;height:72px;margin-bottom:14px}
  .office-address{width:220px;font-size:12.5px;line-height:1.45;color:var(--ink)}
  .office-divider{width:1px;height:58px;background:#9fc9ea;margin:0 24px}
  .office-contacts{list-style:none;font-size:12.5px;color:var(--ink);line-height:1.55}
  .office-contacts li{display:flex;align-items:center;gap:9px}
  .office-contacts svg{width:12px;height:12px;fill:var(--sky);flex:none}
</style>
</head>
<body>

<section class="card card--front" aria-label="Card front">
  <span class="decor-circle"></span>
  <div class="front-lockup">
    <span class="mark-dot"></span>
    <div class="brand-name">Marvella Law</div>
    <span class="rule"></span>
  </div>
</section>

<section class="card card--back" aria-label="Card back">
  <span class="decor-circle"></span>
  <div class="back-lockup">
    <span class="mark-dot"></span>
    <div>
      <div class="brand-name">Marvella Law</div>
      <span class="rule"></span>
    </div>
  </div>

  <div class="offices">
    <div class="office">
      <address class="office-address" style="font-style:normal">118 Harbor Street NW<br>Suite 210, Lakeview<br>MI 49001</address>
      <span class="office-divider"></span>
      <ul class="office-contacts">
        <li><svg viewBox="0 0 24 24"><path d="M6.6 10.8a15 15 0 0 0 6.6 6.6l2.2-2.2c.3-.3.7-.4 1-.2 1.1.4 2.3.6 3.6.6.6 0 1 .4 1 1V20c0 .6-.4 1-1 1A17 17 0 0 1 3 4c0-.6.4-1 1-1h3.5c.6 0 1 .4 1 1 0 1.3.2 2.5.6 3.6.1.3 0 .7-.2 1z"/></svg>555-014-2231</li>
        <li><svg viewBox="0 0 24 24"><path d="M6 2h12v6H6zM4 9h16a2 2 0 0 1 2 2v6h-4v5H6v-5H2v-6a2 2 0 0 1 2-2zm4 8v3h8v-3z"/></svg>555-014-2231</li>
        <li><svg viewBox="0 0 24 24"><path d="M2 5h20v14H2zm2 2v.5l8 5 8-5V7z"/></svg>anna@marvellalaw.com</li>
      </ul>
    </div>
    <div class="office">
      <address class="office-address" style="font-style:normal">118 Harbor Street NW<br>Suite 210, Lakeview<br>MI 49001</address>
      <span class="office-divider"></span>
      <ul class="office-contacts">
        <li><svg viewBox="0 0 24 24"><path d="M6.6 10.8a15 15 0 0 0 6.6 6.6l2.2-2.2c.3-.3.7-.4 1-.2 1.1.4 2.3.6 3.6.6.6 0 1 .4 1 1V20c0 .6-.4 1-1 1A17 17 0 0 1 3 4c0-.6.4-1 1-1h3.5c.6 0 1 .4 1 1 0 1.3.2 2.5.6 3.6.1.3 0 .7-.2 1z"/></svg>555-014-2231</li>
        <li><svg viewBox="0 0 24 24"><path d="M6 2h12v6H6zM4 9h16a2 2 0 0 1 2 2v6h-4v5H6v-5H2v-6a2 2 0 0 1 2-2zm4 8v3h8v-3z"/></svg>555-014-2231</li>
        <li><svg viewBox="0 0 24 24"><path d="M2 5h20v14H2zm2 2v.5l8 5 8-5V7z"/></svg>anna@marvellalaw.com</li>
      </ul>
    </div>
  </div>
</section>

</body>
</html>
```